Charter Tour Boat Webpage Design

We need a web page design for a new business - Saltreef Tackle Tours, We do Fishing Charters, Montague Island Eco Tours, Diving, Whale Watching. We currently have a very basic website up. www.saltreeftackletours.example and as you can see we need a much better one.

Thanks!

Target Market(s)

Mainly fisherman, and families for tours

Industry/Entity Type

Business

Requirements
Must have
• page for fishing, montague island eco tours, whale watching.
Contact page, and enquiry page with form.

```html
<!DOCTYPE html>
<html lang="en">
<head>
<meta charset="utf-8">
<title>Saltreef Tackle Tours</title>
<link href="https://fonts.googleapis.com/css2?family=Arimo:wght@400;700&display=swap" rel="stylesheet">
<style>
  :root {
    --sea: #416fa3;
    --sea-deep: #3a6699;
    --sky: #a9c3e0;
    --brand-blue: #0b9cf4;
    --panel: #ffffff;
    --text: #555555;
    --heading: #2b2b2b;
    --nav-text: #2a2a2a;
    --line: #c9c9c9;
    --arrow-green: #5ccc12;
    --btn-top: #5fcbfc;
    --btn-bottom: #0b95f1;
  }
  * { box-sizing: border-box; margin: 0; padding: 0; }
  html, body { width: 1200px; height: 1172px; overflow: hidden; }
  body {
    position: relative;
    background: var(--sea);
    font-family: "Arimo", Arial, sans-serif;
  }
  .hero {
    position: absolute; left: 0; top: 0; width: 1200px; height: 620px;
    background: linear-gradient(180deg, var(--sky) 0%, #c7d5e3 9%, #c9b795 17%, #b6a98a 24%, #6f8fb5 30%, #4b78ab 40%, #4775a8 70%, var(--sea) 100%);
  }
  .site-name {
    position: absolute; left: 127px; top: 40px;
    font-size: 57px; font-weight: 700; color: var(--brand-blue);
    letter-spacing: -0.5px;
  }
  .gallery { position: absolute; top: 327px; left: 0; }
  .gallery-photo {
    position: absolute; top: 0; width: 216px; height: 197px;
    border: 3px solid #fff; border-radius: 3px;
  }
  .photo-catch { left: 123px; background: linear-gradient(180deg, #7fb7de 0%, #5a8fbb 45%, #3b3a3c 100%); }
  .photo-marlin { left: 366px; background: linear-gradient(160deg, #33466e 0%, #5a6e96 50%, #2c3d63 100%); }
  .photo-lighthouse { left: 614px; background: linear-gradient(180deg, #1f5ea8 0%, #3a7cc2 60%, #7fa35a 100%); }
  .photo-whale { left: 861px; background: linear-gradient(180deg, #2f7f93 0%, #3a8b9b 55%, #2a6f80 100%); }
  .panel {
    position: absolute; left: 127px; top: 539px; width: 946px; height: 570px;
    background: var(--panel);
    box-shadow: 0 2px 8px rgba(0,0,0,0.35);
  }
  .main-nav {
    position: absolute; left: 21px; top: 15px; width: 904px; height: 41px;
    border: 1px solid var(--line); border-radius: 4px;
    background: linear-gradient(180deg, #fbfbfb 0%, #eeeeee 55%, #e2e2e2 100%);
    display: flex; align-items: center; gap: 35px; padding-left: 23px;
    list-style: none;
  }
  .main-nav li { font-size: 16.5px; color: var(--nav-text); letter-spacing: 0.4px; }
  .intro { position: absolute; left: 22px; top: 90px; width: 654px; }
  .intro h1 {
    font-size: 21px; font-weight: 400; color: var(--heading);
    letter-spacing: 0.5px; margin-bottom: 20px;
  }
  .intro p {
    font-size: 15.8px; line-height: 21px; color: var(--text);
    text-align: justify; hyphens: auto; margin-bottom: 21px;
  }
  .side-menu {
    position: absolute; left: 717px; top: 89px; width: 208px;
    border: 1px solid var(--line); list-style: none;
  }
  .side-menu li {
    position: relative; display: flex; align-items: flex-start;
    padding: 11px 0 0 37px;
    font-size: 20.5px; line-height: 24px; color: var(--heading);
    background: linear-gradient(180deg, #f8f8f8 0%, #ebebeb 100%);
    border-top: 1px solid #d8d8d8;
  }
  .side-menu li:first-child { border-top: none; }
  .side-menu li svg { position: absolute; left: 11px; top: 16px; }
  .item-fishing { height: 47px; }
  .item-eco { height: 62px; }
  .item-diving { height: 42px; }
  .item-snorkel { height: 43px; }
  .item-whale { height: 46px; }
  .book-button {
    position: absolute; left: 717px; top: 359px; width: 208px; height: 73px;
    border-radius: 6px;
    background: linear-gradient(180deg, var(--btn-top) 0%, var(--btn-bottom) 100%);
    display: flex; align-items: center; padding-left: 13px;
    color: #fff; font-size: 23.5px; font-weight: 700; letter-spacing: 0.3px;
  }
  .book-button svg { margin-left: 17px; }
  .copyright {
    position: absolute; left: 0; top: 1128px; width: 1200px;
    text-align: center; color: #fff; font-size: 14px;
  }
</style>
</head>
<body>
  <div class="hero" role="img" aria-label="Coastal island with a lighthouse and a whale tail rising from the sea"></div>
  <div class="site-name">Saltreef Tackle Tours</div>

  <div class="gallery">
    <div class="gallery-photo photo-catch" role="img" aria-label="Angler on a boat holding a large fish"></div>
    <div class="gallery-photo photo-marlin" role="img" aria-label="Marlin leaping beside the boat"></div>
    <div class="gallery-photo photo-lighthouse" role="img" aria-label="Island lighthouse on rocks"></div>
    <div class="gallery-photo photo-whale" role="img" aria-label="Whale breaching from the water"></div>
  </div>

  <main class="panel">
    <ul class="main-nav">
      <li>Home</li>
      <li>Fishing</li>
      <li>Montague Island</li>
      <li>Whale Watching</li>
      <li>Book Now</li>
      <li>Contact Us</li>
    </ul>

    <section class="intro">
      <h1>Welcome to Saltreef Tackle Tours!</h1>
      <p>Lorem ipsum dolor sit amet, consectetur adipiscing elit. Duis non augue justo, et elementum justo. Etiam luctus ullamcorper lectus, quis lacinia enim adipiscing ut. Ut mauris elit, fringilla in accumsan sit amet, interdum nec dolor. Etiam viverra tellus elit. Nunc non leo ac eros rutrum bibendum. Ut bibendum enim id ligula adipiscing rutrum. Mauris vestibulum tellus bibendum tellus ultrices non feugiat dolor accumsan. Nulla luctus sapien ac nunc dapibus eu volutpat nibh venenatis. Morbi neque tellus, pharetra eget varius in, fringilla ac sapien, pharetra eget varius in fringilla.</p>
      <p>Lorem ipsum dolor sit amet, consectetur adipiscing elit. Duis non augue justo, et elementum justo. Etiam luctus ullamcorper lectus, quis lacinia enim adipiscing ut. Ut mauris elit, fringilla in accumsan sit amet, interdum nec dolor. Etiam viverra tellus elit. Nunc non leo ac eros rutrum bibendum.</p>
    </section>

    <ul class="side-menu">
      <li class="item-fishing"><svg width="17" height="14" viewBox="0 0 17 14"><path d="M0 0 L17 7 L0 14 L4 7 Z" fill="var(--arrow-green)"/></svg>Fishing</li>
      <li class="item-eco"><svg width="17" height="14" viewBox="0 0 17 14"><path d="M0 0 L17 7 L0 14 L4 7 Z" fill="var(--arrow-green)"/></svg>Montague Island<br>Eco Tours</li>
      <li class="item-diving"><svg width="17" height="14" viewBox="0 0 17 14"><path d="M0 0 L17 7 L0 14 L4 7 Z" fill="var(--arrow-green)"/></svg>Diving</li>
      <li class="item-snorkel"><svg width="17" height="14" viewBox="0 0 17 14"><path d="M0 0 L17 7 L0 14 L4 7 Z" fill="var(--arrow-green)"/></svg>Snorkeling</li>
      <li class="item-whale"><svg width="17" height="14" viewBox="0 0 17 14"><path d="M0 0 L17 7 L0 14 L4 7 Z" fill="var(--arrow-green)"/></svg>Whale Watching</li>
    </ul>

    <div class="book-button">BOOK NOW!<svg width="20" height="23" viewBox="0 0 20 23"><path d="M0 0 L20 11.5 L0 23 Z" fill="#fff"/></svg></div>
  </main>

  <footer class="copyright">Copyright © 2012 Saltreef Tackle Tours</footer>
</body>
</html>
```